Vantrel Telecom Corporate Website & Social Branding

We are looking for a new website for our startup telecom which provides UCaaS, SD-WAN, Business SMS/MMS, Video Conferencing, Managed Network Service & more.

Target Market(s)

Small offices from 1-250 users

Industry/Entity Type

Telecomunications

Coding

Coded - Design and coding required

Colors
0054AA
0677BA
7BADD7
CADEEF
E8F1F8

```html
<!DOCTYPE html>
<html lang="en">
<head>
<meta charset="utf-8">
<title>Vantrel Telecom</title>
<link href="https://fonts.googleapis.com/css2?family=Poppins:wght@400;500;600;700&display=swap" rel="stylesheet">
<style>
:root{
  --blue:#0d8ad6;
  --blue-bright:#1aa1e8;
  --blue-deep:#0054aa;
  --teal:#12c9d0;
  --navy:#112d5c;
  --ink:#1e1e1e;
  --text:#4a4a4a;
  --muted:#f0f3f6;
  --pale:#e8f1f8;
  --white:#ffffff;
}
*{box-sizing:border-box;margin:0;padding:0}
html,body{width:1200px;height:3439px;overflow:hidden}
body{font-family:'Poppins',sans-serif;color:var(--ink);background:var(--white);position:relative}
a{text-decoration:none;color:inherit}
.caret{display:inline-block;width:0;height:0;border-top:4px solid transparent;border-bottom:4px solid transparent;border-left:5px solid currentColor;margin-left:7px;vertical-align:1px}

.topbar{position:absolute;top:0;left:0;width:1200px;height:36px;background:var(--blue-bright);color:#fff;font-size:12px}
.topbar .info{position:absolute;right:172px;top:10px;display:flex;gap:18px}
.topbar span{display:flex;align-items:center;gap:6px}

.nav{position:absolute;top:36px;left:0;width:1200px;height:80px;background:#fff}
.brand{position:absolute;left:172px;top:24px;display:flex;align-items:center;gap:8px;font-weight:700;font-size:22px;color:var(--blue-deep)}
.brand .dot{width:28px;height:28px;border-radius:50%;background:var(--blue)}
.menu{position:absolute;right:172px;top:18px;display:flex;align-items:center;gap:39px;font-size:15px;font-weight:500}
.menu .active{color:var(--blue)}
.btn{display:inline-flex;align-items:center;justify-content:center;font-weight:500;font-size:14px}
.btn-solid{background:var(--blue);color:#fff}
.quote{height:39px;padding:0 17px;margin-left:-16px}

.hero{position:absolute;top:116px;left:0;width:1200px;height:544px;background:linear-gradient(100deg,#1d2b44 0%,#4a5670 45%,#8f8a86 70%,#2d2f3a 100%)}
.hero .photo{position:absolute;inset:0}
.hero .shade{position:absolute;inset:0;background:linear-gradient(90deg,rgba(10,20,40,.55),rgba(10,20,40,0) 60%)}
.hero-text{position:absolute;left:172px;top:152px;color:#fff}
.hero-text .kicker{font-size:24px;font-weight:600;display:flex;align-items:center;gap:10px}
.hero-text .kicker::before{content:"";width:56px;height:2px;background:#fff}
.hero-text h1{font-size:49px;line-height:54px;font-weight:700;margin-top:2px}
.hero-text p{font-size:18px;margin-top:10px}
.hero-btns{display:flex;gap:10px;margin-top:21px}
.hero-btns .btn{height:38px;padding:0 20px;font-size:14px}
.btn-white{background:#fff;color:var(--blue)}
.btn-line{border:2px solid #fff;color:#fff}

.welcome{position:absolute;top:660px;left:0;width:1200px;height:484px}
.welcome .copy{position:absolute;left:172px;top:86px;width:400px}
.welcome .eyebrow{font-size:24px;color:var(--blue)}
.welcome h2{font-size:42px;font-weight:700;line-height:50px}
.welcome p{font-size:14px;line-height:25.5px;color:var(--text);margin-top:16px}
.welcome .btn{height:38px;padding:0 22px;margin-top:30px}
.welcome .visual{position:absolute;left:594px;top:55px;width:474px;height:380px;border-radius:10px;background:linear-gradient(160deg,#3a3f47 0%,#c9a255 45%,#e4e6ea 70%,#cfd3d8 100%)}

.services{position:absolute;top:1144px;left:0;width:1200px;height:418px;background:var(--muted)}
.section-title{text-align:center;font-size:42px;font-weight:700}
.services .section-title{margin-top:26px}
.services .lead{text-align:center;font-size:15px;color:var(--ink);margin-top:4px}
.cards{position:absolute;left:172px;top:151px;display:flex;gap:28px}
.card{width:193px;height:247px;background:#fff;border-radius:6px;box-shadow:0 4px 14px rgba(0,0,0,.08);text-align:center;padding-top:14px}
.card .icon{width:70px;height:70px;border-radius:50%;background:var(--blue);margin:0 auto;display:flex;align-items:center;justify-content:center}
.card h3{font-size:16px;font-weight:600;margin-top:10px}
.card p{font-size:14px;color:var(--text);line-height:28.5px;margin-top:4px}
.card .more{display:inline-block;font-size:14px;color:var(--blue);border-bottom:1px solid var(--blue);margin-top:4px;padding-bottom:1px}

.steps{position:absolute;top:1562px;left:0;width:1200px;height:443px}
.steps .section-title{margin-top:68px}
.steps svg{position:absolute;left:0;top:0}
.step{position:absolute;width:150px;height:150px;border-radius:50%;background:#fff;border:3px solid #dcdcdc;text-align:center;padding-top:27px}
.step .num{font-size:10px;font-weight:600}
.step .num b{color:var(--blue);font-weight:600}
.step h4{font-size:15px;font-weight:600;margin-top:2px}
.step p{font-size:12px;line-height:19px;color:var(--text);margin-top:3px}

.switch{position:absolute;top:2005px;left:0;width:1200px;height:198px;background:linear-gradient(110deg,#1578c6 0%,#2b9be0 55%,#35a8e6 100%)}
.switch h2{position:absolute;left:323px;top:46px;font-size:46px;line-height:52px;color:#fff;font-weight:700}
.switch .btn{position:absolute;left:742px;top:79px;height:37px;width:134px;border:2px solid #fff;color:#fff;font-size:15px}

.news{position:absolute;top:2203px;left:0;width:1200px;height:550px}
.news .section-title{margin-top:38px}
.posts{position:absolute;left:172px;top:131px;display:flex;gap:25px}
.post{width:269px}
.post .thumb{height:180px;border-radius:6px}
.post .date{display:inline-block;margin-top:16px;background:var(--blue);color:#fff;font-size:10px;padding:3px 10px;border-radius:12px}
.post h3{font-size:16px;font-weight:500;margin-top:6px}
.post p{font-size:12px;line-height:20px;color:var(--text);margin-top:2px}
.post .more{display:inline-block;font-size:14px;color:var(--blue);border-bottom:1px solid var(--blue);margin-top:6px}
.next{position:absolute;left:1008px;top:211px;width:36px;height:36px;border-radius:50%;background:var(--blue-bright);display:flex;align-items:center;justify-content:center}

.partners{position:absolute;top:2753px;left:0;width:1200px;height:237px;background:var(--muted)}
.partners .section-title{margin-top:34px}
.logos{position:absolute;left:172px;top:117px;width:856px;display:flex;justify-content:space-between;align-items:center;padding:0 30px}
.logos .mark{width:60px;height:60px}

.footer{position:absolute;top:2990px;left:0;width:1200px;height:449px;background:var(--navy);color:#fff}
.cta{position:absolute;left:258px;top:38px;display:flex;align-items:center}
.cta h2{font-size:44px;font-weight:700;margin-right:32px}
.cta .btn{height:37px;width:127px;font-size:14px}
.cta .btn+.btn{margin-left:8px}
.rule{position:absolute;left:172px;width:856px;height:1px;background:rgba(255,255,255,.3)}
.foot-brand{position:absolute;left:172px;top:206px;display:flex;align-items:center;gap:10px;font-size:24px;font-weight:700}
.foot-brand .dot{width:36px;height:36px;border-radius:50%;background:var(--blue-bright)}
.follow{position:absolute;left:172px;top:293px;display:flex;align-items:center;gap:8px;font-size:14px;font-weight:600}
.follow .soc{width:28px;height:28px;border-radius:50%;background:#fff}
.follow .soc:first-of-type{margin-left:6px}
.col{position:absolute;top:182px;font-size:12px}
.col h5{font-size:14px;font-weight:600;margin-bottom:10px}
.col li{list-style:none;line-height:31.5px;display:flex;align-items:center}
.col li::before{content:"";border-top:3px solid transparent;border-bottom:3px solid transparent;border-left:4px solid var(--blue-bright);margin-right:12px}
.col.contact p{line-height:28px}
.col.contact b{font-weight:600}
.copyright{position:absolute;left:0;width:1200px;top:415px;text-align:center;font-size:13px;color:rgba(255,255,255,.75)}
.copyright b{color:#fff;font-weight:500}
</style>
</head>
<body>

<div class="topbar">
  <div class="info">
    <span><svg width="11" height="11" viewBox="0 0 24 24"><path fill="#fff" d="M6.6 10.8a15.1 15.1 0 0 0 6.6 6.6l2.2-2.2c.3-.3.7-.4 1-.2 1.1.4 2.3.6 3.6.6.6 0 1 .4 1 1V20c0 .6-.4 1-1 1A17 17 0 0 1 3 4c0-.6.4-1 1-1h3.5c.6 0 1 .4 1 1 0 1.3.2 2.5.6 3.6.1.3 0 .7-.2 1z"/></svg>(855) 410-2386</span>
    <span><svg width="12" height="10" viewBox="0 0 24 18"><path fill="#fff" d="M0 0h24v18H0z"/><path fill="none" stroke="#1aa1e8" stroke-width="2" d="M1 1l11 8 11-8"/></svg>hello@vantreltelecom.com</span>
  </div>
</div>

<header class="nav">
  <div class="brand"><span class="dot"></span>Vantrel Telecom</div>
  <nav class="menu">
    <a class="active">Home</a><a>Products</a><a>Solutions</a><a>Pricing</a>
    <a class="btn btn-solid quote">Request A Quote<span class="caret"></span></a>
  </nav>
</header>

<section class="hero">
  <div class="photo" role="img" aria-label="Woman on a phone call working at a laptop in an office"></div>
  <div class="shade"></div>
  <div class="hero-text">
    <div class="kicker">We Provides</div>
    <h1>UCaaS, SD-WAN,<br>Business SMS/MMS,</h1>
    <p>Video Conferencing, Managed Network Service &amp; more</p>
    <div class="hero-btns">
      <a class="btn btn-white">See Pricing<span class="caret"></span></a>
      <a class="btn btn-line">Contact Us<span class="caret"></span></a>
    </div>
  </div>
</section>

<section class="welcome">
  <div class="copy">
    <div class="eyebrow">Welcome to</div>
    <h2>Vantrel Telecom</h2>
    <p>Praesent ultrices blandit lacus. Aliquam feugiat ligula vitae libero varius luctus. Fusce lacinia tellus ut blandit dictum. Curabitur ex est, pharetra at velit quis, vehicula tempor sem. Aliquam consequat magna est, sed</p>
    <a class="btn btn-solid">Read More<span class="caret"></span></a>
  </div>
  <div class="visual" role="img" aria-label="Desktop monitor showing a video conference call beside a desk phone"></div>
</section>

<section class="services">
  <h2 class="section-title">Our Popular Services</h2>
  <p class="lead">Praesent ultrices blandit lacus. Aliquam feugiat ligula vitae libero varius luctus.</p>
  <div class="cards">
    <div class="card">
      <div class="icon"><svg width="38" height="38" viewBox="0 0 40 40" fill="none" stroke="#fff" stroke-width="2"><circle cx="20" cy="13" r="5"/><circle cx="9" cy="17" r="4"/><circle cx="31" cy="17" r="4"/><path d="M10 32c0-6 4-10 10-10s10 4 10 10M2 30c0-4 3-7 7-7M38 30c0-4-3-7-7-7"/></svg></div>
      <h3>UCaaS</h3><p>Fusce lacinia tellus<br>Blandit dictum<br>Pharetra at velit</p><a class="more">Read More<span class="caret"></span></a>
    </div>
    <div class="card">
      <div class="icon"><svg width="38" height="38" viewBox="0 0 40 40" fill="none" stroke="#fff" stroke-width="2"><circle cx="20" cy="20" r="4"/><circle cx="20" cy="5" r="2.5"/><circle cx="20" cy="35" r="2.5"/><circle cx="5" cy="20" r="2.5"/><circle cx="35" cy="20" r="2.5"/><path d="M20 8v8M20 24v8M8 20h8M24 20h8"/></svg></div>
      <h3>SD-WAN</h3><p>Fusce lacinia tellus<br>Blandit dictum<br>Pharetra at velit</p><a class="more">Read More<span class="caret"></span></a>
    </div>
    <div class="card">
      <div class="icon"><svg width="38" height="38" viewBox="0 0 40 40" fill="none" stroke="#fff" stroke-width="2"><rect x="6" y="4" width="22" height="26" rx="3"/><rect x="12" y="10" width="22" height="26" rx="3" fill="#0d8ad6"/><path d="M17 18h12M17 23h12M17 28h8"/></svg></div>
      <h3>Business SMS/MMS</h3><p>Fusce lacinia tellus<br>Blandit dictum<br>Pharetra at velit</p><a class="more">Read More<span class="caret"></span></a>
    </div>
    <div class="card">
      <div class="icon"><svg width="38" height="38" viewBox="0 0 40 40" fill="none" stroke="#fff" stroke-width="2"><rect x="4" y="4" width="32" height="20" rx="2"/><circle cx="13" cy="13" r="3"/><circle cx="27" cy="13" r="3"/><circle cx="20" cy="29" r="3"/><path d="M13 36c0-3 3-4 7-4s7 1 7 4"/></svg></div>
      <h3>Video Conferencing</h3><p>Fusce lacinia tellus<br>Blandit dictum<br>Pharetra at velit</p><a class="more">Read More<span class="caret"></span></a>
    </div>
  </div>
</section>

<section class="steps">
  <svg width="1200" height="443" viewBox="0 0 1200 443">
    <defs>
      <linearGradient id="flow" x1="0" x2="1" y1="0" y2="0">
        <stop offset="0" stop-color="#0a8ad3"/><stop offset="1" stop-color="#12d3cf"/>
      </linearGradient>
    </defs>
    <g fill="none" stroke="url(#flow)" stroke-width="32">
      <path d="M304 173 A100 100 0 1 0 404 273"/>
      <path d="M402 273 A100 100 0 0 1 602 273"/>
      <path d="M598 273 A100 100 0 0 0 798 273"/>
      <path d="M796 273 A100 100 0 0 1 996 273"/>
    </g>
  </svg>
  <h2 class="section-title" style="position:relative">See How it Works</h2>
  <div class="step" style="left:229px;top:198px"><div class="num">STEP <b>01</b></div><h4>Maecenas</h4><p>vehicula tempor sem.<br>Aliquam consequat<br>magna est, sed</p></div>
  <div class="step" style="left:427px;top:198px"><div class="num">STEP <b>02</b></div><h4>Praesent</h4><p>vehicula tempor sem.<br>Aliquam consequat<br>magna est, sed</p></div>
  <div class="step" style="left:623px;top:198px"><div class="num">STEP <b>03</b></div><h4>Fusce lacinia</h4><p>vehicula tempor sem.<br>Aliquam consequat<br>magna est, sed</p></div>
  <div class="step" style="left:821px;top:198px"><div class="num">STEP <b>04</b></div><h4>Curabitur</h4><p>vehicula tempor sem.<br>Aliquam consequat<br>magna est, sed</p></div>
</section>

<section class="switch">
  <h2>Save up to 60%<br>When You Switch</h2>
  <a class="btn">See How<span class="caret"></span></a>
</section>

<section class="news">
  <h2 class="section-title">Latest News</h2>
  <div class="posts">
    <article class="post">
      <div class="thumb" role="img" aria-label="Woman working on a laptop at a desk" style="background:linear-gradient(135deg,#e9ecef,#8aa0bd 60%,#d7dadf)"></div>
      <span class="date">March 16, 2022</span>
      <h3>Donec in sem quam</h3>
      <p>Maecenas eu venenatis arcu. Duis sed sem tincidunt, fermentum felis ut, euismod mauris. Quisque vulputate lacus non</p>
      <a class="more">Read More<span class="caret"></span></a>
    </article>
    <article class="post">
      <div class="thumb" role="img" aria-label="Man on a video call at a laptop by a window" style="background:linear-gradient(135deg,#7d8c9c,#c9cfd6 55%,#a13a4a)"></div>
      <span class="date">March 16, 2022</span>
      <h3>Donec in sem quam</h3>
      <p>Maecenas eu venenatis arcu. Duis sed sem tincidunt, fermentum felis ut, euismod mauris. Quisque vulputate lacus non</p>
      <a class="more">Read More<span class="caret"></span></a>
    </article>
    <article class="post">
      <div class="thumb" role="img" aria-label="Woman waving during a video call on a laptop" style="background:linear-gradient(135deg,#b8885a,#e6d6c4 55%,#6f6a66)"></div>
      <span class="date">March 16, 2022</span>
      <h3>Donec in sem quam</h3>
      <p>Maecenas eu venenatis arcu. Duis sed sem tincidunt, fermentum felis ut, euismod mauris. Quisque vulputate lacus non</p>
      <a class="more">Read More<span class="caret"></span></a>
    </article>
  </div>
  <div class="next"><svg width="12" height="12" viewBox="0 0 12 12"><path d="M4 2l4 4-4 4" fill="none" stroke="#fff" stroke-width="2"/></svg></div>
</section>

<section class="partners">
  <h2 class="section-title">Our Trusted Partners</h2>
  <div class="logos">
    <div class="mark" role="img" aria-label="Partner badge" style="background:#5a5fd8;border-radius:50%"></div>
    <div class="mark" role="img" aria-label="Partner badge" style="background:#3a7bd5;border-radius:12px"></div>
    <div class="mark" role="img" aria-label="Partner badge" style="background:#22b6d6;border-radius:50%"></div>
    <div class="mark" role="img" aria-label="Partner badge" style="background:#4a55c8;border-radius:12px"></div>
    <div class="mark" role="img" aria-label="Partner badge" style="background:#2a8ee0;border-radius:50%"></div>
  </div>
</section>

<footer class="footer">
  <div class="cta">
    <h2>Ready to Switch?</h2>
    <a class="btn btn-solid" style="background:var(--blue-bright)">See Pricing<span class="caret"></span></a>
    <a class="btn btn-line">View Demo<span class="caret"></span></a>
  </div>
  <div class="rule" style="top:134px"></div>
  <div class="foot-brand"><span class="dot"></span>Vantrel Telecom</div>
  <div class="follow">Follow Us
    <span class="soc" role="img" aria-label="Social profile"></span>
    <span class="soc" role="img" aria-label="Social profile"></span>
    <span class="soc" role="img" aria-label="Social profile"></span>
  </div>
  <div class="col contact" style="left:458px">
    <h5>CONTACT INFO</h5>
    <p><b>Direct/SMS:</b> (925) 610-3357</p>
    <p><b>Office:</b> (925) 610-3350</p>
    <p><b>Toll Free:</b> (855) 410-2386</p>
    <p><b>Email:</b> hello@vantreltelecom.com</p>
  </div>
  <div class="col" style="left:736px">
    <h5>QUICK LINKS</h5>
    <ul><li>Home</li><li>Products</li><li>Solutions</li><li>Pricing</li></ul>
  </div>
  <div class="col" style="left:892px">
    <h5>SERVICES</h5>
    <ul><li>UCaaS</li><li>SD-WAN</li><li>Business SMS/MMS</li><li>Video Conferencing</li><li>Managed Network</li></ul>
  </div>
  <div class="rule" style="top:397px"></div>
  <div class="copyright">© 2022 <b>Vantrel Telecom</b> All right reserved</div>
</footer>

</body>
</html>
```